Flyer für eine Tagespflege (Senioren & Demenzkranke)
Zielgruppe
Hallo wir sind eine Tagespflege die 365 Tage im Jahr geöffnet hat. Wir kümmern uns um Senioren und Demenzkranke. Zielgruppe sind Personen die Ihre Angehörigen (zur Entlastung) Zuhause pflegen und Senioren die den Tag in Gemeinschaft verbringen wollen und abends zu Hause im eigenen Bett schlafen wollen
Aufgabenstellung
Es sollte ansprechend bzw. hochwertig aussehen. Es sollte ein Standard Format sein. Bei der Größe gibt es keine Vorgabe. Es sollte übersichtlich sein. Die Adresse sollte mit Karte dargestellt sein. Das wir 365 Tage im Jahr geöffnet haben muss klar hervor gehen.

```html
<!DOCTYPE html>
<html lang="de">
<head>
<meta charset="utf-8">
<title>Tagespflege Keller – Faltblatt</title>
<link rel="stylesheet" href="https://fonts.googleapis.com/css2?family=Open+Sans:ital,wght@0,400;0,600;0,700;1,400&family=Libre+Baskerville:wght@700&display=swap">
<style>
  :root{
    --backdrop:#7fe6ee;
    --paper:#f7f7f7;
    --paper-shade:#c9c9c9;
    --olive:#b4ad56;
    --olive-light:#d2c76a;
    --rule:#d8cc6b;
    --ink:#2e2e2e;
    --cover-ink:#ece6b9;
    --brand:#3a8a3e;
  }
  *{box-sizing:border-box;margin:0;padding:0}
  html,body{width:1200px;height:900px;overflow:hidden}
  body{background:var(--backdrop);font-family:"Open Sans",sans-serif;color:var(--ink);position:relative}
  .spread{position:absolute;left:304px;width:591px;height:420px;display:flex;border-top:2px solid var(--rule);box-shadow:0 6px 18px rgba(0,60,70,.25)}
  .spread--outside{top:20px}
  .spread--inside{top:460px}
  .panel{position:relative;width:197px;height:100%;background:var(--paper);overflow:hidden;font-size:7px;line-height:1.3}
  .panel + .panel{border-left:1px solid #e6e6e6}
  .photo{position:absolute;display:block}
  .rule{position:absolute;height:2px;background:var(--rule)}
  .quote{position:absolute;left:18px;right:18px;top:132px;text-align:center;font-style:italic;font-size:7px;line-height:1.35}
  .brand{position:absolute;left:0;right:0;top:26px;display:flex;align-items:center;justify-content:center;gap:4px;font-weight:700;font-size:7px;color:var(--brand)}
  .brand-dot{width:7px;height:7px;border-radius:50%;background:var(--brand)}
  .intro{position:absolute;left:10px;right:10px;top:130px;text-align:center;font-size:7.6px;line-height:1.25}
  .contact{position:absolute;left:0;right:0;bottom:10px;text-align:center;font-size:6px;line-height:1.3}
  .contact p + p{margin-top:7px}
  .cover-band{position:absolute;left:0;right:0;bottom:0;height:134px;background:var(--olive);padding:48px 12px 0}
  .cover-title{color:var(--cover-ink);font-weight:600;font-size:9.5px;line-height:1.3}
  .cover-sub{color:var(--cover-ink);font-style:italic;font-size:6.5px;margin-top:4px}
  .cover-brand{position:absolute;right:8px;top:18px;background:rgba(255,255,255,.9);padding:6px 5px;display:flex;align-items:center;gap:3px;font-weight:700;font-size:5.5px;color:var(--brand)}
  .label{display:inline-block;background:var(--olive-light);color:#fff;font-family:"Libre Baskerville",serif;font-size:6px;letter-spacing:.5px;text-transform:uppercase;padding:5px 6px;margin-bottom:7px}
  .copy{position:absolute;left:7px;right:7px}
  .copy p + p{margin-top:6px}
  .panel--shaded{background:linear-gradient(180deg,var(--paper) 10%,var(--paper-shade) 100%)}
</style>
</head>
<body>

<section class="spread spread--outside" aria-label="Außenseite">
  <article class="panel">
    <div class="rule" style="left:22px;right:22px;top:120px"></div>
    <p class="quote">Glücklich ist der Mensch,<br>der seinen Nächsten trägt<br>in seiner ganzen Gebrechlichkeit<br>wie er sich wünscht,<br>von jenen getragen zu werden<br>in seiner ganzen Schwäche<br>(Anselm Weidenhof)</p>
    <svg class="photo" style="left:4px;top:276px" width="189" height="140" role="img" aria-label="Foto: Seniorin liest Zeitung am Tisch, Pflegerin steht daneben">
      <defs><linearGradient id="g1" x1="0" y1="0" x2="1" y2="1"><stop offset="0" stop-color="#d9d2c2"/><stop offset="1" stop-color="#b9a994"/></linearGradient></defs>
      <rect width="189" height="140" fill="url(#g1)"/>
    </svg>
  </article>
  <article class="panel">
    <div class="brand"><span class="brand-dot"></span>Tagespflege Keller</div>
    <div class="rule" style="left:30px;right:30px;top:120px"></div>
    <p class="intro">Sie möchten weiterhin in Ihrem Zuhause leben, Selbstbestimmung und Lebensqualität genießen und benötigen dabei Unterstützung? Gemeinsam mit Ihnen besprechen wir ein für Sie passendes Leistungs- und Serviceangebot nach Ihren Wünschen und Bedürfnissen.</p>
    <div class="contact">
      <p>Kontakt / Adresse</p>
      <p>Tagespflege<br>Marta Keller<br>Ahornweg 14<br>17398 Feldbrück</p>
      <p>Telefon 03900/4417280<br>E-Mail tagespflege-mk@beispielpost.de</p>
    </div>
  </article>
  <article class="panel">
    <svg class="photo" style="left:0;top:0" width="197" height="286" role="img" aria-label="Foto: Pflegerin reicht einer Seniorin lächelnd eine Tasse">
      <defs><linearGradient id="g2" x1="0" y1="0" x2="1" y2="1"><stop offset="0" stop-color="#b8c9a3"/><stop offset=".5" stop-color="#e0d6c3"/><stop offset="1" stop-color="#6f8a72"/></linearGradient></defs>
      <rect width="197" height="286" fill="url(#g2)"/>
    </svg>
    <div class="cover-brand"><span class="brand-dot" style="width:5px;height:5px"></span>Tagespflege Keller</div>
    <div class="cover-band">
      <h1 class="cover-title">Tagespflege des<br>Ambulanten Pflegedienstes</h1>
      <p class="cover-sub">365 Tage Betreuung</p>
    </div>
  </article>
</section>

<section class="spread spread--inside" aria-label="Innenseite">
  <article class="panel panel--shaded">
    <svg class="photo" style="left:4px;top:0" width="189" height="138" role="img" aria-label="Foto: Pflegerin und Senior sitzen lachend im Garten">
      <defs><linearGradient id="g3" x1="0" y1="0" x2="1" y2="1"><stop offset="0" stop-color="#a9c08a"/><stop offset="1" stop-color="#6d7a5a"/></linearGradient></defs>
      <rect width="189" height="138" fill="url(#g3)"/>
    </svg>
    <div class="copy" style="top:148px">
      <span class="label">Unsere Tagespflege</span>
      <p>Sie fühlen sich in Ihrem Zuhause wohl möchten oder können dort aber nicht den gesamten Tag über alleine sein? Unsere Tagespflege bietet Ihnen behaglich eingerichtete Räumlichkeiten, nette Gesellschaft und Abwechslung.</p>
      <p>Als <b>Tagesgast</b> in unserer 2017 eröffneten Einrichtung erwartet Sie hier täglich wechselnde sinnvolle <b>Betreuungsangebote</b> mit verschiedenen Aktivitäten, die auf jeden Tagesgast <b>individuell abgestimmt</b> sind. Das abwechslungsreiche Freizeitprogramm können Sie nach Ihren Wünschen wahrnehmen oder sich zwischendurch zurückziehen und Abgeschiedenheit und Ruhe genießen.</p>
      <p>Unsere Tagespflege ist als einzige in Feldbrück an <b>365 Tagen im Jahr geöffnet</b>!</p>
    </div>
  </article>
  <article class="panel">
    <div class="copy" style="top:40px">
      <span class="label">Leistungen</span>
      <p>Mit unserer Tagespflege schließen wir die Lücke zwischen <b>Häuslichkeit</b> und <b>Pflegeheim</b>.</p>
      <p>Wir unterstützen unsere Gäste dabei, im Rahmen ihrer individuellen Fähigkeiten und Wünsche <b>selbstbestimmt</b> am Leben teilzunehmen und <b>aktiv</b> zu sein.<br>Ihre Angehörigen werden gleichzeitig entlastet und können in Ruhe arbeiten. Besuchen Sie unser Gästehaus und schauen Sie sich um.</p>
      <p>Im <b>persönlichen Gespräch</b> beraten wir Sie vor Ort zu unseren Leistungen. Auf Wunsch vereinbaren Sie einen Termin. Gern können Sie dann, für ihren Angehörigen einen <b>kostenlosen Schnuppertag</b> in unserer Tagesspflege festlegen.</p>
    </div>
    <svg class="photo" style="left:6px;bottom:0" width="185" height="130" role="img" aria-label="Foto: heller Gemeinschaftsraum mit Küche und Esstischen">
      <defs><linearGradient id="g4" x1="0" y1="0" x2="0" y2="1"><stop offset="0" stop-color="#f2ece2"/><stop offset="1" stop-color="#c8b59a"/></linearGradient></defs>
      <rect width="185" height="130" fill="url(#g4)"/>
    </svg>
  </article>
  <article class="panel">
    <svg class="photo" style="left:0;top:0" width="92" height="115" role="img" aria-label="Foto: Hand setzt Spielfigur auf ein Brettspiel">
      <rect width="92" height="115" fill="#e6d8bf"/>
    </svg>
    <svg class="photo" style="left:96px;top:0" width="101" height="115" role="img" aria-label="Foto: Teller mit geschnittenem Obst">
      <rect width="101" height="115" fill="#e9d9a8"/>
    </svg>
    <div class="copy" style="top:126px">
      <span class="label">Unser Team</span>
      <p>Das Team der Tagespflege besteht aus <b>12 erfahrenen und hoch motivierten Mitarbeitern</b>, die sich um Ihr Wohl kümmern.</p>
      <p>Auf Wunsch holen wir Sie morgens zu Hause ab und bringen Sie am Nachmittag zurück.<br>Bei der Betreuung und Tagesgestaltung stehen Ihre <b>individuellen Wünsche</b> und <b>Fähigkeiten</b> an erster Stelle. Gemeinsame Ausflüge, Bewegungsübungen, Spiele oder Kochen sorgen für <b>Abwechslung plus Spaß</b> und lassen keinen Tag lang werden.</p>
    </div>
    <svg class="photo" style="left:0;bottom:0" width="197" height="134" role="img" aria-label="Foto: Pflegeteam in grünen Poloshirts auf einem Weg im Grünen">
      <defs><linearGradient id="g5" x1="0" y1="0" x2="0" y2="1"><stop offset="0" stop-color="#8fae72"/><stop offset="1" stop-color="#9a9a8e"/></linearGradient></defs>
      <rect width="197" height="134" fill="url(#g5)"/>
    </svg>
  </article>
</section>

</body>
</html>
```